New Architectural Firm Business Cards

New Business card to compliment previous pixel forum logo (attached). Please design a business card that is simple, modern, creative....please do not use "symbols", simply the logo and associated graphics/text. The front should contain name/address/phone/email/web address (with graphics).....back should be 100% graphic design using the logo somehow. Hoping for a two color (black and yellow) design. full bleed design, no borders

Target Market(s)

Commercial Architecture Clients

Industry/Entity Type

Architecture

Contact Information for Business Card

Please design a business card that is simple, modern, creative....please do not use "symbols", simply the logo and associated graphics/text. The front should contain name/address/phone/email/web address (with graphics).....back should be 100% graphic design using the logo somehow

Font styles to use
Sans Serif

Colors
FFF300
FFF600
FEFA6F
FFFEC7
FFFEE8

Requirements
Must have
• Clean, Modern Design
Should not have
• Stock images or "icons"

```html
<!DOCTYPE html>
<html lang="en">
<head>
<meta charset="utf-8">
<title>pixel forum – Business Card</title>
<link href="https://fonts.googleapis.com/css2?family=Montserrat:wght@400;700&display=swap" rel="stylesheet">
<style>
  :root {
    --card-black: #0a0b09;
    --brand-yellow: #f7c515;
    --text-white: #ffffff;
    --page-bg: #ffffff;
  }
  * { margin: 0; padding: 0; box-sizing: border-box; }
  html, body {
    width: 1200px;
    height: 1000px;
    overflow: hidden;
    background: var(--page-bg);
    font-family: "Montserrat", Arial, sans-serif;
  }
  .canvas { position: relative; width: 1200px; height: 1000px; }
  .card {
    position: absolute;
    top: 110px;
    width: 507px;
    height: 289px;
    background: var(--card-black);
    overflow: hidden;
  }
  .card--front { left: 73px; }
  .card--back { left: 620px; }
  .speed-lines { position: absolute; top: 0; right: 0; }
  .contact-name {
    position: absolute;
    left: 40px;
    top: 124px;
    color: var(--brand-yellow);
    font-weight: 700;
    font-size: 23px;
    line-height: 1;
  }
  .contact-role {
    position: absolute;
    left: 40px;
    top: 152px;
    color: var(--text-white);
    font-size: 15px;
    line-height: 1;
  }
  .contact-details {
    position: absolute;
    left: 40px;
    top: 189px;
    list-style: none;
    color: var(--text-white);
    font-size: 12px;
    line-height: 16px;
  }
  .brand-mark {
    position: absolute;
    left: 0;
    width: 507px;
    top: 120px;
    text-align: center;
    color: var(--brand-yellow);
    font-weight: 700;
    font-size: 40px;
    line-height: 1;
    letter-spacing: -0.5px;
  }
</style>
</head>
<body>
<main class="canvas">
  <section class="card card--front" aria-label="Business card front">
    <h1 class="contact-name">Lorem Ipsum</h1>
    <p class="contact-role">Loremipsum</p>
    <ul class="contact-details">
      <li>Address: Location Lorem</li>
      <li>Tel: +44 0123 4560</li>
      <li>Web: www.website.com</li>
      <li>Email: email@website.com</li>
    </ul>
    <svg class="speed-lines" width="120" height="289" viewBox="0 0 120 289" aria-hidden="true">
      <g fill="var(--brand-yellow)">
        <rect x="74" y="81" width="46" height="4"/>
        <rect x="13" y="115" width="107" height="4"/>
        <rect x="74" y="145" width="46" height="4"/>
        <rect x="13" y="175" width="107" height="4"/>
        <rect x="74" y="203" width="46" height="4"/>
      </g>
    </svg>
  </section>

  <section class="card card--back" aria-label="Business card back">
    <p class="brand-mark">pixel forum</p>
    <svg class="speed-lines" width="120" height="289" viewBox="0 0 120 289" aria-hidden="true">
      <g fill="var(--brand-yellow)">
        <rect x="74" y="81" width="46" height="4"/>
        <rect x="13" y="115" width="107" height="4"/>
        <rect x="74" y="145" width="46" height="4"/>
        <rect x="13" y="175" width="107" height="4"/>
        <rect x="74" y="203" width="46" height="4"/>
      </g>
    </svg>
  </section>
</main>
</body>
</html>
```